Logo for a gospel Ministry
Logo for a gospel ministry
Project: Logo for a gospel Ministry
Professional
Neema Tuvako & Halida Ruth Sesiwa
Harvesters
P.O Box 27350 Arusha Tanzania
neemahalida42@postmeadow.example

```html
<!DOCTYPE html>
<html lang="en">
<head>
<meta charset="utf-8">
<title>Gracefield House Ministry – Business Card</title>
<link href="https://fonts.googleapis.com/css2?family=Montserrat:wght@400;500;700&display=swap" rel="stylesheet">
<style>
  :root {
    --backdrop: #e9eaee;
    --royal-blue: #1f3f9c;
    --card-white: #ffffff;
    --gold: #c9a23a;
    --ink-blue: #1f3f9c;
    --text-light: #ffffff;
    --text-soft: #d6def5;
  }
  * { box-sizing: border-box; margin: 0; padding: 0; }
  html, body {
    width: 1200px; height: 874px; overflow: hidden;
    background: var(--backdrop);
    font-family: "Montserrat", Arial, sans-serif;
  }
  .stage { position: relative; width: 1200px; height: 874px; }
  .card {
    position: absolute; width: 560px; height: 320px;
    border-radius: 22px; overflow: hidden;
    box-shadow: 0 10px 30px rgba(20, 30, 60, 0.18);
  }
  .card-front {
    left: 540px; top: 90px; background: var(--royal-blue);
    display: flex; align-items: center; justify-content: center;
  }
  .card-back {
    left: 100px; top: 460px; background: var(--card-white);
    display: flex;
  }
  .brand { display: flex; align-items: center; gap: 14px; }
  .brand-dot { width: 34px; height: 34px; border-radius: 50%; flex: none; }
  .brand-name { font-weight: 700; line-height: 1.15; }
  .card-front .brand-dot { background: var(--text-light); }
  .card-front .brand-name { color: var(--text-light); font-size: 30px; }
  .card-back .brand-dot { background: var(--gold); width: 26px; height: 26px; }
  .card-back .brand-name { color: var(--ink-blue); font-size: 21px; }
  .back-logo-side {
    width: 230px; display: flex; align-items: center; justify-content: center;
    padding-left: 16px;
  }
  .gold-divider { width: 7px; background: var(--gold); margin: 0 0 0 4px; }
  .back-info-side {
    flex: 1; background: var(--royal-blue); color: var(--text-light);
    padding: 62px 30px 0 34px;
  }
  .holder-names { font-weight: 700; font-size: 17px; line-height: 1.3; }
  .holder-role { font-size: 11px; color: var(--text-soft); margin-top: 4px; }
  .address { font-size: 12px; margin-top: 22px; line-height: 1.5; }
  .contact-row { display: flex; align-items: center; gap: 8px; font-size: 12px; margin-top: 5px; }
  .contact-row svg { width: 12px; height: 12px; flex: none; }
  .contacts { margin-top: 8px; }
</style>
</head>
<body>
<div class="stage">
  <section class="card card-front">
    <div class="brand">
      <span class="brand-dot"></span>
      <span class="brand-name">Gracefield House<br>Ministry</span>
    </div>
  </section>

  <section class="card card-back">
    <div class="back-logo-side">
      <div class="brand">
        <span class="brand-dot"></span>
        <span class="brand-name">Gracefield House<br>Ministry</span>
      </div>
    </div>
    <div class="gold-divider"></div>
    <div class="back-info-side">
      <p class="holder-names">Neema Tuvako &amp;<br>Halida Ruth Sesiwa</p>
      <p class="holder-role">Harvesters</p>
      <p class="address">P.O Box 27350<br>Arusha Tanzania</p>
      <div class="contacts">
        <div class="contact-row">
          <svg viewBox="0 0 12 12"><rect x="3" y="0.5" width="6" height="11" rx="1.2" fill="none" stroke="#fff" stroke-width="1.2"/><circle cx="6" cy="9.5" r="0.7" fill="#fff"/></svg>
          <span>+255713208846</span>
        </div>
        <div class="contact-row">
          <svg viewBox="0 0 12 12"><rect x="3" y="0.5" width="6" height="11" rx="1.2" fill="none" stroke="#fff" stroke-width="1.2"/><circle cx="6" cy="9.5" r="0.7" fill="#fff"/></svg>
          <span>+255689471205</span>
        </div>
        <div class="contact-row">
          <svg viewBox="0 0 12 12"><rect x="0.8" y="2.5" width="10.4" height="7" fill="none" stroke="#fff" stroke-width="1.1"/><path d="M0.8 2.5 L6 6.6 L11.2 2.5" fill="none" stroke="#fff" stroke-width="1.1"/></svg>
          <span>neemahalida42@postmeadow.example</span>
        </div>
      </div>
    </div>
  </section>
</div>
</body>
</html>
```